Professional Website for Commercial Real Estate Broker

I own a small boutique commercial real estate company called Harbinridge Realty.
My current website is www.movewithquorl.com and is hosted on hostelmira. I am looking for an all new website that will allow me to compete with bigger players in our industry. In other words, I need something professional, sleek, and functional.

I am looking for a designer that can take my complete website all the way to coding, migration, and launch. I understand that this may be an add'l charge, so please include with your design submission what the add'l charge will be to take the website to launch with all functionality as described below.

As an example of a page in my industry that I like please check out: www.tobiaskellner.com.

My logo is attached and my main colors are the blue, white, grey - similar to the logo.

I am looking for a five page website with the following pages:

Home
Harbinridge Team
Services
Sold Properties
Contact

A couple of features that I will want on the site are:

- I want to make sure that we can imbed a news commercial real estate news feed from: http://www.bizplotwire.com/news/ on the website's home page, similar to how it is on tobiaskellner.com.

- Sold Properties page will allow me to upload the following information on to the website so that I can add new properties that I have recently sold on a weekly or monthly basis. I would like the information to be displayed similarly to http://www.tobiaskellner.com/properties.html . I should be able to upload: picture, price, bldg size, lot size, closing date for each property. This will require a user friendly back end that I can navigate.

- On the home page, I also want to have a form where visitors can request a Market Analysis of their property by entering: Name, property address, email address, phone number. I will be sent an email with this information and I can follow up via telephone or email direct.

- The Harbinridge Team page will have a picture, contact info, and brief bio for each member of the team. I would like to be able to adjust this on a user friendly back end.

I have included my Company Logo. Feel free to use any text from my current website: www.movewithquorl.com. Also, any sleek looking stock photos of office / commercial buildings can be used for the initial design purposes.

I look forward to getting your design submittal and moving forward asap!

Target Market(s)

Los Angeles real estate brokers, developers, and investors.

Industry/Entity Type

Real Estate

Coding

Coded - Design and coding required

Number of Pages Required

5+ page

Font styles to use
Sans Serif

Colors
ffffff
85abd2
0455a3
b2b2b2
000000
3276b5

Requirements
Must have
• Sleek and professional design.
• - I want to make sure that we can imbed a news commercial real estate news feed from: http://www.bizplotwire.com/news/ on the website's home page, similar to how it is on tobiaskellner.com.
• - Sold Properties page will allow me to upload the following information on to the website so that I can add new properties that I have recently sold on a weekly or monthly basis. I would like the information to be displayed similarly to http://www.tobiaskellner.com/properties.html . I should be able to upload: picture, price, bldg size, lot size, closing date for each property. This will require a user friendly back end that I can navigate.
• - On the home page, I also want to have a form where visitors can request a Market Analysis of their property by entering: Name, property address, email address, phone number. I will be sent an email with this information and I can follow up via telephone or email direct.
Nice to have
• Dynamic banner on the home page with beautiful photos that change every few seconds.

```html
<!DOCTYPE html>
<html lang="en">
<head>
<meta charset="utf-8">
<title>Harbinridge Realty — Commercial Real Estate</title>
<link rel="stylesheet" href="https://fonts.googleapis.com/css2?family=Open+Sans:wght@300;400;600;700&family=Rubik:wght@700&display=swap">
<style>
:root{
  --white:#ffffff;
  --sky:#85abd2;
  --navy:#0455a3;
  --mid:#3276b5;
  --grey:#b2b2b2;
  --ink:#000000;
  --text:#555b62;
  --link:#5b8fc7;
  --line:#e4e7ea;
}
*{margin:0;padding:0;box-sizing:border-box}
html,body{width:1200px;height:2609px;overflow:hidden;background:var(--white)}
body{font-family:"Open Sans",Arial,sans-serif;color:var(--text);position:relative}
.abs{position:absolute}

/* header */
.site-header{position:absolute;left:0;top:0;width:1200px;height:87px;background:var(--white);box-shadow:0 2px 6px rgba(0,0,0,.12);z-index:2}
.brand{position:absolute;left:132px;top:26px;display:flex;align-items:center;gap:10px;color:var(--navy);font-weight:700;font-size:20px;letter-spacing:.5px}
.brand-mark{width:24px;height:24px;background:var(--grey)}
.main-nav{position:absolute;right:132px;top:36px;display:flex;gap:40px;font-size:12px;letter-spacing:.4px}
.main-nav a{color:#555;text-decoration:none}
.main-nav a.active{color:var(--navy);font-weight:600}

/* hero */
.hero{position:absolute;left:0;top:87px;width:1200px;height:525px;
  background:linear-gradient(180deg,#a9c0d6 0%,#8aa6bf 12%,#55708a 30%,#3f5f7c 45%,#6c7a82 65%,#7d7f80 100%)}
.hero-tagline{position:absolute;left:136px;top:257px;width:500px;height:105px;background:rgba(150,160,170,.72);
  color:var(--white);font-family:"Rubik","Open Sans",sans-serif;font-weight:700;font-size:24px;line-height:30px;padding:24px 20px}
.analysis-form{position:absolute;left:765px;top:157px;width:301px;height:379px;background:rgba(133,171,210,.92);padding:24px 28px 0}
.analysis-form h2{color:var(--white);font-size:16px;font-weight:700;text-align:center;line-height:21px;margin-bottom:18px}
.field{height:35px;background:var(--white);font-size:12px;color:#555;padding:10px 14px;margin-bottom:12px}
.submit{margin-top:12px;height:46px;background:var(--navy);color:var(--white);font-weight:700;font-size:17px;text-align:center;line-height:46px}
.slider-dots{position:absolute;left:560px;top:554px;display:flex;gap:8px}
.slider-dots span{width:14px;height:14px;border-radius:50%;background:var(--white)}
.slider-dots span.current{background:transparent;border:2px solid var(--white)}

/* welcome */
.section-title{position:absolute;left:0;width:1200px;text-align:center;font-weight:300;color:var(--mid);font-size:42px}
.copy{position:absolute;left:180px;width:840px;text-align:center;font-size:13.5px;line-height:23px;color:#444}
.btn-outline{position:absolute;height:51px;border:2px solid var(--mid);color:var(--mid);font-size:13px;font-weight:600;text-align:center;line-height:47px;letter-spacing:.3px}

/* about */
.about-band{position:absolute;left:0;top:1054px;width:1200px;height:374px;
  background:linear-gradient(100deg,#2f68a8 0%,#4a7fbc 40%,#3a72b2 70%,#2a63a2 100%)}
.about-band .section-title{color:var(--white);top:64px}
.about-band .copy{color:var(--white);top:135px;left:200px;width:800px;font-size:12px;line-height:23px}
.about-band .btn-outline{border-color:var(--white);color:var(--white)}

/* news */
.news-item{position:absolute;left:132px;width:936px;height:151px;border-bottom:1px solid var(--line)}
.news-thumb{position:absolute;left:0;top:0;width:150px;height:84px}
.news-title{position:absolute;left:186px;top:6px;font-size:17px;color:var(--link)}
.news-excerpt{position:absolute;left:186px;top:40px;font-size:11.5px;color:#777}
.news-date{position:absolute;left:186px;top:68px;font-size:11px;color:#555}
.btn-solid{position:absolute;left:527px;top:2167px;width:144px;height:40px;background:var(--mid);color:var(--white);font-size:11.5px;font-weight:600;text-align:center;line-height:40px}

/* footer */
.site-footer{position:absolute;left:0;top:2289px;width:1200px;height:320px;background:var(--navy);color:var(--white)}
.site-footer h3{position:absolute;top:40px;font-size:17px;font-weight:600}
.site-footer ul{list-style:none;position:absolute;font-size:13.5px;line-height:29.5px}
.divider{position:absolute;top:40px;width:1px;height:150px;background:rgba(255,255,255,.15)}
.contact-line{position:absolute;left:470px;font-size:14px;line-height:24px;display:flex;align-items:center;gap:10px}
.subscribe{position:absolute;left:764px;top:104px;display:flex}
.subscribe .email{width:206px;height:36px;background:var(--white);color:#aaa;font-size:12px;padding:11px 14px}
.subscribe .go{width:98px;height:36px;background:var(--sky);color:var(--white);font-size:13px;text-align:center;line-height:36px}
.social{position:absolute;left:764px;top:153px;display:flex;gap:11px}
.social span{width:36px;height:36px;border-radius:50%;background:var(--white)}
.footer-rule{position:absolute;left:132px;top:253px;width:936px;height:1px;background:rgba(255,255,255,.45)}
.copyright{position:absolute;left:132px;top:271px;font-size:13px}
</style>
</head>
<body>

<header class="site-header">
  <div class="brand"><span class="brand-mark"></span>HARBINRIDGE</div>
  <nav class="main-nav">
    <a class="active">HOME</a><a>HARBINRIDGE TEAM</a><a>SERVICES</a><a>SOLD PROPERTIES</a><a>CONTACT</a>
  </nav>
</header>

<section class="hero" role="img" aria-label="Aerial photo of a waterfront city with office buildings and a lake">
</section>
<div class="hero-tagline">We are a small boutique commercial real estate company.</div>
<form class="analysis-form">
  <h2>REQUEST A MARKET ANALYSIS<br>OF THEIR PROPERTY</h2>
  <div class="field">Your name</div>
  <div class="field">Property address</div>
  <div class="field">Email address</div>
  <div class="field">Phone number</div>
  <div class="submit">SUBMIT NOW!</div>
</form>
<div class="slider-dots"><span class="current"></span><span></span><span></span><span></span></div>

<h1 class="section-title" style="top:664px">Welcome to Harbinridge Realty</h1>
<p class="copy" style="top:740px">Harbinridge Realty is a commercial real estate brokerage firm that provides a range of services to assist each of our clients in reaching their real estate objectives quickly and efficiently.</p>
<p class="copy" style="top:804px">Our focus on Southern California investment properties allows us to have a unique and focused perspective on this highly competitive market. Through our experience, diligence and resourcefulness, we help our clients make informed real estate decisions with their specific goals in mind.</p>
<div class="btn-outline" style="left:489px;top:918px;width:222px">READ MORE INFORMATION</div>

<section class="about-band" role="img" aria-label="Blue-tinted photo of a business handshake in front of office towers">
  <h2 class="section-title">About Harbinridge Realty</h2>
  <p class="copy">Harbinridge Realty brings local expertise and hands on customer service to each and every transaction. Each of our clients gets specific attention to their particular goals and objectives. We are a client-based real estate firm and we rely heavily on our strong reputation within the industry.<br><br>Our focus on Southern California investment properties allows us to have a unique and focused perspective in this highly competitive market.</p>
  <div class="btn-outline" style="left:485px;top:257px;width:228px;height:46px;line-height:42px">READ MORE INFORMATION</div>
</section>

<h2 class="section-title" style="top:1464px">Latest News</h2>

<article class="news-item" style="top:1560px">
  <div class="news-thumb" role="img" aria-label="City skyline photo" style="background:linear-gradient(180deg,#b9d3ea,#6f7d86)"></div>
  <div class="news-title">A Major Distraction': Is A Mega-Deal Like Norvane's ...</div>
  <div class="news-excerpt">On a wall in Dale Penhurst's office is a frame with a custom-engraved wrench and a photo of workers ...</div>
  <div class="news-date">Oct 18, 2017 8:52 AM</div>
</article>
<article class="news-item" style="top:1711px">
  <div class="news-thumb" role="img" aria-label="Photo of hands working with a calculator and documents" style="background:linear-gradient(135deg,#c98a5a,#ece4dc)"></div>
  <div class="news-title">Norvane has brought benefits- and disruption- to Seattle</div>
  <div class="news-excerpt">Norvane has brought benefits- and disruption- to Seattle By MARK OLSTED Coastal Wire CW Photo...</div>
  <div class="news-date">Oct 18, 2017 7:37 AM</div>
</article>
<article class="news-item" style="top:1862px">
  <div class="news-thumb" role="img" aria-label="Photo of a calculator and pen on paperwork" style="background:linear-gradient(135deg,#4b5057,#a6abb0)"></div>
  <div class="news-title">Augmented Reality and drones win NY real estate hack...</div>
  <div class="news-excerpt">Dozens of innovators in technology and real estate spent last weekend in a fourth-floor midtown M...</div>
  <div class="news-date">Oct 17, 2017 8:05 PM</div>
</article>
<article class="news-item" style="top:2013px;border-bottom:none">
  <div class="news-thumb" role="img" aria-label="Photo of a bright glass office interior" style="background:linear-gradient(135deg,#7fb8dc,#e7eef3)"></div>
  <div class="news-title">Gridline Works chooses Toronto for its high-tech urba...</div>
  <div class="news-excerpt">Gridline Works, the urban innovation unit of Parallax Holdings, Searchly's parent company, announced during a...</div>
  <div class="news-date">Oct 17, 2017 7:26 PM</div>
</article>
<div class="btn-solid">VIEW MORE NEWS ›</div>

<footer class="site-footer">
  <h3 style="left:132px">QUICK LINKS</h3>
  <ul style="left:132px;top:73px"><li>Home</li><li>Harbinridge Team</li><li>Services</li><li>Sold Properties</li><li>Contact</li></ul>
  <ul style="left:301px;top:73px"><li>Terms of Service</li><li>Privacy Policy</li><li>FAQ's</li></ul>
  <div class="divider" style="left:432px"></div>
  <h3 style="left:470px">CONTACT INFO</h3>
  <div class="contact-line" style="top:80px">4870 Lindell Ave., Suite 212<br>Sherwood Glen, CA 91480</div>
  <div class="contact-line" style="top:132px">
    <svg width="13" height="13" viewBox="0 0 16 16"><rect x="1" y="1" width="14" height="14" rx="3" fill="#fff"/><path d="M5 4l2 2-1 1.2c.7 1.4 1.6 2.3 2.8 2.8L10 9l2 2-1.2 1.2C7.5 12 4 8.5 3.8 5.2z" fill="#0455a3"/></svg>818.555.0142</div>
  <div class="contact-line" style="top:163px">
    <svg width="14" height="11" viewBox="0 0 16 12"><rect width="16" height="12" rx="1.5" fill="#fff"/><path d="M1 1.5l7 5 7-5" stroke="#0455a3" stroke-width="1.5" fill="none"/></svg>hello@harbinridge-mail.com</div>
  <div class="divider" style="left:730px"></div>
  <h3 style="left:762px">SIGN UP FOR NEWSLETTERS</h3>
  <div class="abs" style="left:762px;top:72px;font-size:13px">Please sign up here for latest news</div>
  <div class="subscribe"><div class="email">EMAIL ADDRESS</div><div class="go">SUBSCRIBE</div></div>
  <div class="social"><span></span><span></span><span></span><span></span></div>
  <div class="footer-rule"></div>
  <div class="copyright">© 2017 HARBINRIDGE REALTY.&nbsp; All right reserved . Term of Use</div>
</footer>

</body>
</html>
```